Pictures to represent a consulting company and their main topics

We need around 10 pictures which can be used in blogs, webpages, powerpoints or articles to prettify and visualize the content.
We are a business consulting company in the financial industry.
We are based in and focussed on Switzerland.
Our main colours are blue turquise and grey (see www.veltrano.example).
The main topics, we would like to use the pictures for are:
- Digitalization
- Regulations
- Agile Project Management
- Advisory Process
- Automated System Testing
The price is for 10 pictures (which should be similar and therefore are not considered as 10 independent projects).
We propose to start with 3 example pictures to agree on the style. The rest will then be similar ones of the same style.
I have added examples from other companies.
It can be based on stock images or (prefferably) sketched images. Important is that the style is always the same.
Target Market(s)
Banking and Banking Consulting Market Switzerland
Industry/Entity Type
Business

```html
<!DOCTYPE html>
<html lang="en">
<head>
<meta charset="utf-8">
<title>Regulations – Veltrano</title>
<link rel="stylesheet" href="https://fonts.googleapis.com/css2?family=Noto+Sans:wght@400&family=Cinzel:wght@400&display=swap">
<style>
  :root {
    --paper: #ffffff;
    --navy: #2f4a7a;
    --slate-blue: #4a6497;
    --ink: #111111;
    --teal: #1ea39c;
    --teal-deep: #138a85;
    --magenta: #b84f9a;
    --plum: #8a2166;
  }
  html, body {
    margin: 0;
    padding: 0;
    overflow: hidden;
    background: var(--paper);
  }
  .slide {
    position: relative;
    width: 1200px;
    height: 864px;
    overflow: hidden;
    background: var(--paper);
    font-family: "Noto Sans", Verdana, sans-serif;
    color: var(--ink);
  }
  .brand {
    position: absolute;
    left: 26px;
    top: 36px;
    display: flex;
    align-items: center;
    gap: 16px;
  }
  .brand-mark {
    width: 40px;
    height: 40px;
    background: var(--navy);
  }
  .brand-name {
    font-family: "Cinzel", Georgia, serif;
    font-size: 50px;
    line-height: 1;
    letter-spacing: 3px;
    color: var(--navy);
  }
  .title {
    position: absolute;
    left: 74px;
    top: 104px;
    margin: 0;
    font-weight: 400;
    font-size: 88px;
    line-height: 1.1;
    color: var(--slate-blue);
  }
  .intro {
    position: absolute;
    left: 78px;
    top: 226px;
    width: 720px;
    margin: 0;
    font-size: 37px;
    line-height: 59px;
  }
  .benefits {
    position: absolute;
    left: 84px;
    top: 452px;
    width: 680px;
    margin: 0;
    padding: 0;
    list-style: none;
    font-size: 30px;
    line-height: 38px;
  }
  .benefits li {
    position: relative;
    padding-left: 62px;
    margin-bottom: 62px;
  }
  .benefits li:nth-child(2) { margin-bottom: 64px; }
  .benefits li::before {
    content: "";
    position: absolute;
    left: 0;
    top: 50%;
    width: 33px;
    height: 33px;
    margin-top: -16px;
    border-radius: 50%;
    background: var(--slate-blue);
  }
  .benefits li:first-child::before { top: 37px; }
  .info-figure {
    position: absolute;
    left: 850px;
    top: 34px;
    width: 328px;
    height: 780px;
    border-radius: 40px;
    background: linear-gradient(180deg, var(--magenta) 0%, var(--teal) 35%, var(--teal-deep) 70%, var(--magenta) 100%);
    opacity: 0.85;
  }
  .base-band {
    position: absolute;
    left: 338px;
    top: 793px;
    width: 862px;
    height: 71px;
    background: var(--teal-deep);
  }
</style>
</head>
<body>
  <main class="slide">
    <header class="brand">
      <span class="brand-mark"></span>
      <span class="brand-name">VELTRANO</span>
    </header>

    <h1 class="title">Regulations</h1>

    <p class="intro">This is where you would have information relating to what you are discussing.</p>

    <ul class="benefits">
      <li>Bullet points express a clear benefit and promise to the reader</li>
      <li>Easier on the eyes</li>
      <li>Easier on the reader.</li>
    </ul>

    <div class="info-figure" role="img" aria-label="Abstract illustration of an information letter i formed by a magenta dot and folded turquoise and magenta ribbons"></div>

    <div class="base-band"></div>
  </main>
</body>
</html>
```